Candidate Table Page

Need our intranet page redesigned. The layout is perfect and doesn't need to change. But the whole page doesn't seem to fit well together. Please change the font, feel, and table borders to make a more professional and easy user interface. symbols and/or icons are okay.

Target Market(s)

company staff

Industry/Entity Type

Security Guard

Coding

Coded - Design and coding required

Number of Pages Required

1 page

Font styles to use
Sans Serif

Colors
0255a3
fece3e

Requirements
Must have
• the employee information and columns
Nice to have
• icons and maybe symbols.

```html
<!DOCTYPE html>
<html lang="en">
<head>
<meta charset="utf-8">
<title>Candidates — Sentinel Watch Services</title>
<link href="https://fonts.googleapis.com/css2?family=Figtree:wght@400;600;700;800&display=swap" rel="stylesheet">
<style>
:root{
  --brand-blue:#0255a3;
  --brand-yellow:#fece3e;
  --page-bg:#f1f1f3;
  --row-alt:#ededf0;
  --line:#dcdde2;
  --text:#2b2b33;
  --muted:#555a66;
  --white:#ffffff;
}
*{box-sizing:border-box;margin:0;padding:0}
html,body{width:1200px;height:654px;overflow:hidden}
body{font-family:"Figtree",sans-serif;background:var(--page-bg);color:var(--text);position:relative;font-size:9.5px}
.topbar{position:absolute;left:0;top:0;width:1200px;height:77px;background:var(--brand-blue)}
.brand{position:absolute;left:24px;top:24px;display:flex;align-items:center;gap:8px}
.brand-dot{width:26px;height:26px;border-radius:50%;background:var(--brand-yellow)}
.brand-name{color:var(--brand-yellow);font-weight:800;font-size:15px;line-height:15px;text-transform:uppercase;width:140px}
.search-label{position:absolute;left:244px;top:13px;color:var(--white);font-size:9.5px}
.field{position:absolute;top:29px;height:28px;background:var(--white);display:flex;align-items:center;padding:0 9px;font-size:9.5px;color:var(--text);justify-content:space-between}
.field svg{flex:none}
.field-by{left:244px;width:94px;border-right:1px solid var(--line)}
.field-query{left:338px;width:262px}
.field-query .tools{display:flex;gap:8px}
.field-job{left:651px;width:121px;border-right:1px solid var(--line)}
.field-status{left:772px;width:128px;border-right:1px solid var(--line);justify-content:space-between;padding-left:29px}
.field-office{left:900px;width:107px;padding-left:23px}
.avatar{position:absolute;left:1055px;top:19px;width:38px;height:38px;border-radius:50%;background:linear-gradient(#f4f4f6,#c9ccd3)}
.user-name{position:absolute;left:1107px;top:21px;color:var(--white);font-size:11px}
.logout{position:absolute;left:1108px;top:40px;width:43px;height:14px;background:var(--brand-yellow);color:var(--text);font-size:9px;display:flex;align-items:center;justify-content:center}
.sidenav{position:absolute;left:9px;top:98px;width:155px;height:471px;background:var(--white);box-shadow:0 0 3px rgba(0,0,0,.15)}
.nav-item{height:33.4px;display:flex;align-items:center;padding:0 10px 0 12px;border-bottom:1px solid var(--line);font-size:10px;color:var(--text)}
.nav-item .label{flex:1;margin-left:10px}
.nav-item.active{background:var(--brand-blue);color:var(--white);font-weight:600;height:34px}
.grid{position:absolute;left:178px;top:100px;width:1006px;height:469px;background:var(--white);box-shadow:0 0 3px rgba(0,0,0,.12)}
table{border-collapse:collapse;table-layout:fixed;width:1006px}
th{background:var(--brand-blue);color:var(--white);font-weight:700;font-size:8.5px;height:30px;text-align:center;border-right:1px solid rgba(255,255,255,.35);text-transform:uppercase}
th:last-child{border-right:none}
td{height:28.6px;padding:0 8px;border-right:1px solid var(--line);white-space:nowrap;overflow:hidden;font-size:9.2px}
td:last-child{border-right:none}
tbody tr:nth-child(even){background:var(--row-alt)}
td.c-created,td.c-status,td.c-notes{text-align:center}
td.c-phone,td.c-cell{padding:0 5px}
.pager{position:absolute;left:178px;top:578px;width:1006px;height:26px;background:#e9e9ec;border:1px solid var(--line);display:flex;align-items:center;font-size:9.5px;color:var(--muted)}
.pager .nav{display:flex;align-items:center;gap:6px;margin-left:18px;margin-right:6px}
.page{width:18px;height:24px;display:flex;align-items:center;justify-content:center;border-right:1px solid var(--line)}
.page.current{width:14px;height:17px;background:var(--brand-yellow);color:var(--text);margin:0 2px;border:none}
.page.wide{width:22px}
.per-size{margin-left:20px;margin-right:10px;color:var(--text)}
.size-select{width:50px;height:24px;background:var(--white);display:flex;align-items:center;justify-content:space-between;padding:0 9px;color:var(--text);border-left:1px solid var(--line);border-right:1px solid var(--line)}
.totals{margin-left:auto;margin-right:8px;display:flex;align-items:center;gap:4px;color:var(--text)}
.count{background:var(--brand-blue);color:var(--white);font-weight:700;padding:2px 4px}
.footer{position:absolute;left:0;width:1200px;top:625px;text-align:center;font-size:9px;color:var(--text)}
</style>
</head>
<body>
<header class="topbar">
  <div class="brand"><span class="brand-dot"></span><span class="brand-name">Sentinel Watch Services</span></div>
  <div class="search-label">Search by</div>
  <div class="field field-by">Names <svg width="8" height="5" viewBox="0 0 8 5"><path d="M1 1l3 3 3-3" fill="none" stroke="#333" stroke-width="1.2"/></svg></div>
  <div class="field field-query">Search
    <span class="tools">
      <svg width="15" height="15" viewBox="0 0 15 15"><circle cx="6" cy="6" r="5" fill="none" stroke="#0255a3" stroke-width="1.5"/><path d="M9.8 9.8L14 14" stroke="#0255a3" stroke-width="1.6"/></svg>
      <svg width="14" height="15" viewBox="0 0 14 15"><path d="M4 2L1 5l3 3M1 5h8a4 4 0 010 8H3" fill="none" stroke="#0255a3" stroke-width="1.4"/></svg>
    </span>
  </div>
  <div class="field field-job">Job <svg width="8" height="5" viewBox="0 0 8 5"><path d="M1 1l3 3 3-3" fill="none" stroke="#333" stroke-width="1.2"/></svg></div>
  <div class="field field-status">Status <svg width="8" height="5" viewBox="0 0 8 5"><path d="M1 1l3 3 3-3" fill="none" stroke="#333" stroke-width="1.2"/></svg></div>
  <div class="field field-office">Office <svg width="8" height="5" viewBox="0 0 8 5"><path d="M1 1l3 3 3-3" fill="none" stroke="#333" stroke-width="1.2"/></svg></div>
  <div class="avatar" role="img" aria-label="User profile photo placeholder"></div>
  <div class="user-name">Lena Marsh</div>
  <div class="logout">Logout</div>
</header>

<nav class="sidenav">
  <div class="nav-item active"><svg width="9" height="9" viewBox="0 0 10 10"><path d="M5 1L1 5h1.5v4h2V7h1v2h2V5H9z" fill="#fece3e"/></svg><span class="label">Home</span></div>
  <div class="nav-item"><svg width="9" height="10" viewBox="0 0 9 10"><circle cx="4.5" cy="4" r="3" fill="none" stroke="#555" stroke-width="1"/><path d="M3 8h3" stroke="#555"/></svg><span class="label">Human Resource</span><svg width="8" height="5" viewBox="0 0 8 5"><path d="M1 1l3 3 3-3" fill="none" stroke="#555" stroke-width="1.1"/></svg></div>
  <div class="nav-item"><svg width="10" height="9" viewBox="0 0 10 9"><rect x="0.5" y="2" width="9" height="6.5" fill="#555"/><rect x="3.5" y="0.5" width="3" height="2" fill="none" stroke="#555"/></svg><span class="label">Recruiting</span><svg width="8" height="5" viewBox="0 0 8 5"><path d="M1 1l3 3 3-3" fill="none" stroke="#555" stroke-width="1.1"/></svg></div>
  <div class="nav-item"><svg width="10" height="9" viewBox="0 0 10 9"><path d="M1 5l2-4h4l2 4v3H1z" fill="none" stroke="#555"/></svg><span class="label">Inventory</span><svg width="8" height="5" viewBox="0 0 8 5"><path d="M1 1l3 3 3-3" fill="none" stroke="#555" stroke-width="1.1"/></svg></div>
  <div class="nav-item"><svg width="10" height="10" viewBox="0 0 10 10"><rect x="0.5" y="1.5" width="7" height="8" fill="none" stroke="#555"/><path d="M4 6l5-5" stroke="#555"/></svg><span class="label">Contracts</span><svg width="8" height="5" viewBox="0 0 8 5"><path d="M1 1l3 3 3-3" fill="none" stroke="#555" stroke-width="1.1"/></svg></div>
  <div class="nav-item"><svg width="10" height="7" viewBox="0 0 10 7"><ellipse cx="5" cy="3.5" rx="4.5" ry="3" fill="#555"/><circle cx="5" cy="3.5" r="1.3" fill="#fff"/></svg><span class="label">Supervision</span><svg width="8" height="5" viewBox="0 0 8 5"><path d="M1 1l3 3 3-3" fill="none" stroke="#555" stroke-width="1.1"/></svg></div>
  <div class="nav-item"><svg width="9" height="10" viewBox="0 0 9 10"><path d="M0.5 0.5h5l3 3v6h-8z" fill="#555"/></svg><span class="label">Reports</span><svg width="8" height="5" viewBox="0 0 8 5"><path d="M1 1l3 3 3-3" fill="none" stroke="#555" stroke-width="1.1"/></svg></div>
  <div class="nav-item"><svg width="10" height="10" viewBox="0 0 10 10"><circle cx="5" cy="5" r="3.3" fill="none" stroke="#555" stroke-width="2.2" stroke-dasharray="2 1"/></svg><span class="label">Settings</span><svg width="8" height="5" viewBox="0 0 8 5"><path d="M1 1l3 3 3-3" fill="none" stroke="#555" stroke-width="1.1"/></svg></div>
  <div class="nav-item"><svg width="11" height="9" viewBox="0 0 11 9"><path d="M0.5 0v8.5H11M2 8l3-4 2 2 3-4v6z" fill="#555" stroke="#555" stroke-width=".6"/></svg><span class="label">Organisation Chart</span><svg width="8" height="5" viewBox="0 0 8 5"><path d="M1 1l3 3 3-3" fill="none" stroke="#555" stroke-width="1.1"/></svg></div>
</nav>

<section class="grid">
<table>
<colgroup>
<col style="width:74px"><col style="width:165px"><col style="width:83px"><col style="width:77px"><col style="width:125px"><col style="width:51px"><col style="width:41px"><col style="width:148px"><col style="width:52px"><col style="width:50px"><col style="width:50px"><col style="width:90px">
</colgroup>
<thead><tr><th>Created</th><th>Name</th><th>Phone#</th><th>Cell#</th><th>City, State</th><th>Status</th><th>Notes</th><th>Reason</th><th>Reactive</th><th>Retest</th><th>Rehire</th><th>Job Position</th></tr></thead>
<tbody>
<tr><td class="c-created">23-Jun-2017</td><td>Omar Vance</td><td class="c-phone">(780)-555-0148</td><td class="c-cell">(760)555-0171</td><td>Hesperia.California</td><td class="c-status">Qualified</td><td class="c-notes">Notes</td><td></td><td></td><td></td><td></td><td>Un-Armed Guard</td></tr>
<tr><td class="c-created">23-Jun-2017</td><td>Dale Monroe</td><td class="c-phone">(510)-555-0192</td><td class="c-cell">(510)-555-0137</td><td>San Leandro.California</td><td class="c-status">Qualified</td><td class="c-notes">Notes</td><td></td><td></td><td></td><td></td><td>Un-Armed Guard</td></tr>
<tr><td class="c-created">22-Jun-2017</td><td>Marla Keene</td><td class="c-phone">(206)-555-0116</td><td class="c-cell">(206)-555-0116</td><td>Kent.Washington</td><td class="c-status">Pending</td><td class="c-notes">Notes</td><td></td><td></td><td></td><td></td><td>Attendant</td></tr>
<tr><td class="c-created">22-Jun-2017</td><td>Tessa Joan Harlow</td><td class="c-phone">(310)555-0124</td><td class="c-cell">(323)555-0185</td><td>Compton.California</td><td class="c-status">Qualified</td><td class="c-notes">Notes</td><td></td><td></td><td></td><td></td><td>Un-Armed Guard</td></tr>
<tr><td class="c-created">22-Jun-2017</td><td>Victor Allen Lane Moreau</td><td class="c-phone">(714)555-0102</td><td class="c-cell">(714)555-0159</td><td>Los Angeles.California</td><td class="c-status">Qualified</td><td class="c-notes">Notes</td><td></td><td></td><td></td><td></td><td>Un-Armed Guard</td></tr>
<tr><td class="c-created">22-Jun-2017</td><td>Gavin Reid Holt-Parry</td><td class="c-phone">(310)-555-0163</td><td class="c-cell">(310)555-0163</td><td>Los Angeles.California</td><td class="c-status">Qualified</td><td class="c-notes">Notes</td><td></td><td></td><td></td><td></td><td>Un-Armed Guard</td></tr>
<tr><td class="c-created">22-Jun-2017</td><td>Nina Poole</td><td class="c-phone">(206)-555-0179</td><td class="c-cell">(206)555-0179</td><td>Renton.Washington</td><td class="c-status">Qualified</td><td class="c-notes">Notes</td><td></td><td></td><td></td><td></td><td>Attendant</td></tr>
<tr><td class="c-created">22-Jun-2017</td><td>Felipe Ortega</td><td class="c-phone">(323)-555-0141</td><td class="c-cell">(323)555-0106</td><td>Maywood.California</td><td class="c-status">Qualified</td><td class="c-notes">Notes</td><td></td><td></td><td></td><td></td><td>Armed Guard</td></tr>
<tr><td class="c-created">22-Jun-2017</td><td>Joy Lynne Carver</td><td class="c-phone">(323)-555-0133</td><td class="c-cell">(323)-555-0194</td><td>Los Angeles.California</td><td class="c-status">Qualified</td><td class="c-notes">Notes</td><td></td><td></td><td></td><td></td><td>Un-Armed Guard</td></tr>
<tr><td class="c-created">22-Jun-2017</td><td>Owen Brantley</td><td class="c-phone">(323)-555-0127</td><td class="c-cell">(323)-555-0150</td><td>Los Angeles.California</td><td class="c-status">Qualified</td><td class="c-notes">Notes</td><td></td><td></td><td></td><td></td><td>Un-Armed Guard</td></tr>
<tr><td class="c-created">22-Jun-2017</td><td>Camille Renee Ashford</td><td class="c-phone">(707)-555-0181</td><td class="c-cell">(707)-555-0181</td><td>Vallejo.California</td><td class="c-status">Qualified</td><td class="c-notes">Notes</td><td></td><td></td><td></td><td></td><td>Un-Armed Guard</td></tr>
<tr><td class="c-created">22-Jun-2017</td><td>Kemi A. Adeyemi-O</td><td class="c-phone">(424)-555-0112</td><td class="c-cell">(424)555-0112</td><td>Lynwood.California</td><td class="c-status">Qualified</td><td class="c-notes">Notes</td><td></td><td></td><td></td><td></td><td>Un-Armed Guard</td></tr>
<tr><td class="c-created">22-Jun-2017</td><td>Marcus T Bell</td><td class="c-phone">(832)-555-0168</td><td class="c-cell">(832)-555-0168</td><td>Houston.Toas</td><td class="c-status">Qualified</td><td class="c-notes">Notes</td><td></td><td></td><td></td><td></td><td>Armed Guard</td></tr>
<tr><td class="c-created">22-Jun-2017</td><td>Renee K Pratt</td><td class="c-phone">(310)-555-0145</td><td class="c-cell">(310)555-0199</td><td>Corona.California</td><td class="c-status">Qualified</td><td class="c-notes">Notes</td><td></td><td></td><td></td><td></td><td>Un-Armed Guard</td></tr>
<tr><td class="c-created">22-Jun-2017</td><td>Sandra Whitfield</td><td class="c-phone">(206)555-0173</td><td class="c-cell">(206)555-0173</td><td>Kent.Washington</td><td class="c-status">Schedule</td><td class="c-notes">Notes</td><td></td><td></td><td></td><td></td><td>Un-Armed Guard</td></tr>
</tbody>
</table>
</section>

<div class="pager">
  <span class="nav">
    <svg width="10" height="8" viewBox="0 0 10 8"><path d="M5 1L2 4l3 3M9 1L6 4l3 3" fill="none" stroke="#0255a3" stroke-width="1.4"/></svg>
    <svg width="6" height="8" viewBox="0 0 6 8"><path d="M5 1L2 4l3 3" fill="none" stroke="#0255a3" stroke-width="1.4"/></svg>
  </span>
  <span class="page current">1</span><span class="page">2</span><span class="page">3</span><span class="page">4</span><span class="page">5</span><span class="page wide">6</span><span class="page">7</span><span class="page wide">8</span><span class="page">9</span><span class="page wide">10</span>
  <span class="nav" style="margin-left:8px">
    <svg width="6" height="8" viewBox="0 0 6 8"><path d="M1 1l3 3-3 3" fill="none" stroke="#0255a3" stroke-width="1.4"/></svg>
    <svg width="10" height="8" viewBox="0 0 10 8"><path d="M1 1l3 3-3 3M5 1l3 3-3 3" fill="none" stroke="#0255a3" stroke-width="1.4"/></svg>
  </span>
  <span class="per-size">Page per size</span>
  <span class="size-select">15 <svg width="8" height="5" viewBox="0 0 8 5"><path d="M1 1l3 3 3-3" fill="none" stroke="#333" stroke-width="1.1"/></svg></span>
  <span class="totals"><span class="count">336</span> items in <span class="count">225</span> pages</span>
</div>

<footer class="footer">Copyrights @ 2017 Sentinel Watch Services All Rights Reserved</footer>
</body>
</html>
```